KTM Law Firm Business Card

We need a business card design for our law firm. We recently had a name change and so we have a new logo. We are a small plaintiff's law firm in Oklahoma but do work all over the USA We have a new logo (see attached the artwork in both black & brown – could also reverse the logo so that it’s white) We'd like an upscale western design. One side needs the logo and this slogan : "Integrity-Grit-Resolve Always stand your ground"
and on the other side needs to be a template so we can fill in the attorney's name --include this info:
Whitcombe Whitcombe Delacroix
-------Attorneys------------
(name of attorney) ie: Howard T. Whitcombe
(title) ie: Attorney/Managing Partner
5382 S. Garnet Tulsa, OK 74129
918-555-0143
Fax 918-555-0187
(name)@ktmlaw-example.com www.ktmlaw-example.com ie: howie@ktmlaw-example.com
also needs a small Chatterbook & chirpnet logo -
and 3 of the attorneys need the circle logo attached that says "Premier Verdict Counsel Circle" - so we need to be able to remove that for some of the designs –

```html
<!DOCTYPE html>
<html lang="en">
<head>
<meta charset="utf-8">
<title>WWD Law Firm Business Card</title>
<link rel="stylesheet" href="https://fonts.googleapis.com/css2?family=Open+Sans:wght@400;600;700&display=swap">
<style>
  :root {
    --page-bg: #e9e6e1;
    --card-black: #0d0d0d;
    --card-black-soft: #1e1e1e;
    --card-white: #ffffff;
    --ink: #1a1a1a;
    --ink-grey: #6a6a6a;
    --silver: #c9c9c9;
    --slogan: #f2f2f2;
    --badge: #7a1420;
    --badge-ring: #c9a44a;
    --band: #111111;
    --band-line: #9a9a9a;
  }
  * { margin: 0; padding: 0; box-sizing: border-box; }
  html, body { width: 1200px; height: 784px; overflow: hidden; }
  body {
    background: var(--page-bg);
    font-family: "Open Sans", Arial, sans-serif;
    position: relative;
  }
  .card {
    position: absolute;
    width: 560px;
    height: 320px;
    border-radius: 4px;
    box-shadow: 0 6px 18px rgba(0,0,0,0.25);
    overflow: hidden;
  }

  /* Back side */
  .card-back {
    left: 50px;
    top: 60px;
    background: radial-gradient(ellipse at 50% 30%, var(--card-black-soft) 0%, var(--card-black) 70%);
  }
  .card-back .firm-mark {
    position: absolute;
    left: 0; right: 0;
    top: 96px;
    text-align: center;
    color: var(--silver);
    font-weight: 700;
    font-size: 40px;
    letter-spacing: 3px;
    text-transform: uppercase;
  }
  .card-back .firm-rule {
    position: absolute;
    left: 180px; right: 180px;
    top: 158px;
    height: 1px;
    background: var(--silver);
  }
  .card-back .slogan {
    position: absolute;
    left: 36px;
    right: 36px;
    bottom: 44px;
    color: var(--slogan);
    font-size: 14px;
    letter-spacing: 3px;
    font-variant: small-caps;
    white-space: nowrap;
  }

  /* Front side */
  .card-front {
    left: 590px;
    top: 404px;
    background: var(--card-white);
  }
  .card-front .attorney {
    position: absolute;
    right: 26px;
    top: 24px;
    text-align: right;
  }
  .card-front .attorney-name {
    color: var(--ink-grey);
    font-weight: 700;
    font-size: 19px;
    line-height: 1.1;
  }
  .card-front .attorney-title {
    color: var(--ink);
    font-size: 10.5px;
    margin-top: 3px;
  }
  .card-front .firm-mark {
    position: absolute;
    left: 30px;
    top: 78px;
    display: flex;
    align-items: center;
    gap: 10px;
  }
  .card-front .firm-mark .dot {
    width: 14px; height: 14px;
    border-radius: 50%;
    background: var(--ink);
  }
  .card-front .firm-mark .name {
    color: var(--ink);
    font-weight: 700;
    font-size: 26px;
    letter-spacing: 2px;
    text-transform: uppercase;
  }
  .contact-list {
    position: absolute;
    left: 30px;
    top: 150px;
    list-style: none;
  }
  .contact-list li {
    display: flex;
    align-items: center;
    gap: 9px;
    color: var(--ink);
    font-size: 14px;
    height: 21px;
  }
  .contact-list svg {
    width: 14px; height: 14px;
    fill: var(--ink-grey);
    flex: none;
  }
  .badge {
    position: absolute;
    right: 28px;
    top: 112px;
    width: 62px; height: 62px;
    border-radius: 50%;
    background: var(--badge);
    border: 3px solid var(--badge-ring);
  }
  .front-band {
    position: absolute;
    left: 0; right: 0;
    bottom: 0;
    height: 34px;
    background: var(--band);
    border-top: 3px solid var(--band-line);
  }
</style>
</head>
<body>

<section class="card card-back" aria-label="Card back">
  <div class="firm-mark">WWD Law Firm</div>
  <div class="firm-rule"></div>
  <p class="slogan">Integrity-Grit-Resolve Always stand your ground</p>
</section>

<section class="card card-front" aria-label="Card front">
  <div class="attorney">
    <div class="attorney-name">Howard T. Whitcombe</div>
    <div class="attorney-title">Attorney/Managing Partner</div>
  </div>

  <div class="firm-mark">
    <span class="dot"></span>
    <span class="name">WWD Law Firm</span>
  </div>

  <ul class="contact-list">
    <li>
      <svg viewBox="0 0 16 16"><path d="M8 0a5.5 5.5 0 0 0-5.5 5.5C2.5 10 8 16 8 16s5.5-6 5.5-10.5A5.5 5.5 0 0 0 8 0zm0 8a2.5 2.5 0 1 1 0-5 2.5 2.5 0 0 1 0 5z"/></svg>
      5382 S. Garnet Tulsa, OK 74129
    </li>
    <li>
      <svg viewBox="0 0 16 16"><path d="M3.6 1.2l2.2 2.6c.3.4.3.9 0 1.3L4.7 6.4c.9 2 2.6 3.8 4.7 4.8l1.3-1.2c.4-.3.9-.3 1.3 0l2.6 2.1c.4.3.4.9.1 1.3l-1.3 1.4c-.6.6-1.5.8-2.3.5C6 13.6 2.5 10 .9 5.2.6 4.4.8 3.5 1.4 2.9L2.3 1.1c.4-.3.9-.3 1.3.1z"/></svg>
      918-555-0143
    </li>
    <li>
      <svg viewBox="0 0 16 16"><path d="M4 1h8v4H4zM2 6h12a1 1 0 0 1 1 1v5h-3v3H4v-3H1V7a1 1 0 0 1 1-1zm3 6v2h6v-2z"/></svg>
      918-555-0187
    </li>
    <li>
      <svg viewBox="0 0 16 16"><path d="M1 3h14v10H1zm1.5 1.5v.4L8 8.8l5.5-3.9v-.4zm0 2.2v4.8h11V6.7L8 10.6z"/></svg>
      howie@wwdlaw-example.com
    </li>
    <li>
      <svg viewBox="0 0 16 16"><path d="M8 0a8 8 0 1 0 0 16A8 8 0 0 0 8 0zm5.9 7.3h-2.6a12 12 0 0 0-1-4.9 6.5 6.5 0 0 1 3.6 4.9zM8 1.6c.8 1 1.6 3 1.8 5.7H6.2C6.4 4.6 7.2 2.6 8 1.6zM5.7 2.4a12 12 0 0 0-1 4.9H2.1a6.5 6.5 0 0 1 3.6-4.9zM2.1 8.7h2.6a12 12 0 0 0 1 4.9 6.5 6.5 0 0 1-3.6-4.9zM8 14.4c-.8-1-1.6-3-1.8-5.7h3.6c-.2 2.7-1 4.7-1.8 5.7zm2.3-.8a12 12 0 0 0 1-4.9h2.6a6.5 6.5 0 0 1-3.6 4.9z"/></svg>
      www.wwdlaw-example.com
    </li>
  </ul>

  <div class="badge" role="img" aria-label="Premier Verdict Counsel Circle membership badge"></div>

  <div class="front-band"></div>
</section>

</body>
</html>
```